vacuumfood jar modern packaging for design product

the design should be modern and simple. As seen in the target market, the jar can be used by mothers for their babies, but also for workers in offices and outdoor fanatics. package dimensions: 10.5 x 10.5 x 17.0 cm

Target Market(s)

food jar for mothers / baby food on the other hand modern design for food jars in everday use (work, outdoors, ...)

Industry/Entity Type

Product

Font styles to use
Sans Serif

Colors

Designer to choose colors to be used in the design.

Requirements
Must have
• We would like to have one side in german and one side in english front: Calendo Food Jar (thermo food container) back: vacuum food jar information / characteristics: no BPA stainless steel copper coating hot / cold for up to 24 h (see example hot cold.pic) - voblo logo - www.voblo.eu - symbol "food contact material" - EAN barcode - 450 ml / 15,2 oz importanp: do not microwave, not for dishwasher - can be pictograms / icons
Should not have
• No picture of the real product on the package

```html
<!DOCTYPE html>
<html lang="de">
<head>
<meta charset="utf-8">
<title>voblo – Thermospeisebehälter Verpackung</title>
<link href="https://fonts.googleapis.com/css2?family=Roboto+Condensed:wght@300;400&display=swap" rel="stylesheet">
<style>
  :root {
    --stage: #e4e4e4;
    --carton: #57575c;
    --carton-dark: #4d4d52;
    --accent: #e87722;
    --ink-light: #ffffff;
    --ink-soft: #d9d9dc;
  }
  * { box-sizing: border-box; margin: 0; padding: 0; }
  html, body { width: 1200px; height: 666px; overflow: hidden; }
  body {
    background: var(--stage);
    font-family: "Roboto Condensed", Arial, sans-serif;
    color: var(--ink-light);
  }
  .dieline {
    position: absolute; left: 150px; top: 106px;
    display: flex; gap: 30px;
  }
  .panel {
    position: relative; width: 280px; height: 454px;
    background: var(--carton);
    overflow: hidden;
  }
  .band {
    position: absolute; top: 96px; height: 40px; background: var(--accent);
  }
  .band--left { left: 0; width: 52px; }
  .band--right { right: 0; width: 52px; }
  .band--full { left: 0; right: 0; }
  .panel--side .band--full { left: 0; width: 100%; }

  .brand {
    position: absolute; top: 92px; left: 0; right: 0;
    text-align: center; font-weight: 300; font-size: 46px; line-height: 48px;
    letter-spacing: 1px; color: var(--ink-light);
  }
  .title {
    position: absolute; top: 178px; left: 0; right: 0; text-align: center;
    font-size: 20px; font-weight: 400;
  }
  .subtitle {
    position: absolute; top: 204px; left: 0; right: 0; text-align: center;
    font-size: 15px; font-weight: 300; color: var(--ink-soft);
  }
  .product-art {
    position: absolute; left: 76px; top: 240px; width: 128px; height: 168px;
    border-radius: 26px 26px 30px 30px;
    background: linear-gradient(180deg, #6a5a50 0%, #5e5450 100%);
    border: 1px solid rgba(232,119,34,.45);
  }
  .volume {
    position: absolute; top: 420px; left: 0; right: 0; text-align: center;
    font-size: 9px; font-weight: 300; color: var(--ink-soft);
  }

  /* side with features */
  .side-brand {
    position: absolute; left: 22px; top: 440px;
    transform: rotate(-90deg); transform-origin: left top;
    font-size: 64px; font-weight: 300; line-height: 64px; color: var(--accent);
  }
  .features {
    position: absolute; left: 118px; top: 160px; list-style: none;
  }
  .features li {
    display: flex; align-items: center; gap: 8px; height: 34px;
    font-size: 9px; font-weight: 300; color: var(--ink-soft);
  }
  .icon {
    width: 20px; height: 20px; flex: none;
  }
  .web {
    position: absolute; left: 118px; bottom: 22px;
    font-size: 9px; color: var(--accent);
  }
  .rule {
    position: absolute; left: 110px; bottom: 40px; width: 1px; height: 300px;
    background: rgba(255,255,255,.25);
  }

  /* side with marks */
  .marks {
    position: absolute; left: 22px; bottom: 22px; display: flex; gap: 14px;
  }
  .mark { display: flex; flex-direction: column; align-items: center; gap: 4px;
    font-size: 7px; font-weight: 300; color: var(--ink-soft); }
</style>
</head>
<body>
<main class="dieline">

  <section class="panel panel--side" aria-label="Seitenansicht Eigenschaften">
    <div class="band band--full"></div>
    <div class="side-brand">voblo</div>
    <div class="rule"></div>
    <ul class="features">
      <li><svg class="icon" viewBox="0 0 20 20"><circle cx="10" cy="10" r="9" fill="none" stroke="#d9d9dc"/><line x1="4" y1="16" x2="16" y2="4" stroke="#d9d9dc"/></svg>no BPA</li>
      <li><svg class="icon" viewBox="0 0 20 20"><circle cx="10" cy="10" r="9" fill="none" stroke="#d9d9dc"/><polyline points="6,10 9,13 14,7" fill="none" stroke="#d9d9dc"/></svg>stainless steel</li>
      <li><svg class="icon" viewBox="0 0 20 20"><circle cx="10" cy="10" r="9" fill="none" stroke="#d9d9dc"/><circle cx="10" cy="10" r="4" fill="none" stroke="#d9d9dc"/></svg>copper coating</li>
      <li><svg class="icon" viewBox="0 0 20 20"><circle cx="10" cy="10" r="9" fill="none" stroke="#d9d9dc"/><line x1="10" y1="5" x2="10" y2="15" stroke="#d9d9dc"/></svg>hot 24 h</li>
      <li><svg class="icon" viewBox="0 0 20 20"><circle cx="10" cy="10" r="9" fill="none" stroke="#d9d9dc"/><line x1="5" y1="10" x2="15" y2="10" stroke="#d9d9dc"/><line x1="10" y1="5" x2="10" y2="15" stroke="#d9d9dc"/></svg>cold 24 h</li>
      <li><svg class="icon" viewBox="0 0 20 20"><circle cx="10" cy="10" r="9" fill="none" stroke="#d9d9dc"/><rect x="6" y="7" width="8" height="6" fill="none" stroke="#d9d9dc"/><line x1="4" y1="16" x2="16" y2="4" stroke="#d9d9dc"/></svg>no microwave</li>
      <li><svg class="icon" viewBox="0 0 20 20"><circle cx="10" cy="10" r="9" fill="none" stroke="#d9d9dc"/><rect x="6" y="6" width="8" height="8" fill="none" stroke="#d9d9dc"/><line x1="4" y1="16" x2="16" y2="4" stroke="#d9d9dc"/></svg>no dishwasher</li>
    </ul>
    <div class="web">www.voblo.eu</div>
  </section>

  <section class="panel panel--front" aria-label="Vorderseite">
    <div class="band band--left"></div>
    <div class="band band--right"></div>
    <div class="brand">voblo</div>
    <h1 class="title">Thermospeisebehälter</h1>
    <p class="subtitle">- thermo speise behälter -</p>
    <div class="product-art" role="img" aria-label="Orange line illustration of the food jar with handle and lid button"></div>
    <p class="volume">450 ml / 15,2 oz</p>
  </section>

  <section class="panel panel--side" aria-label="Seitenansicht Hinweise">
    <div class="band band--full"></div>
    <div class="marks">
      <div class="mark"><svg class="icon" viewBox="0 0 20 20"><circle cx="10" cy="10" r="9" fill="none" stroke="#d9d9dc"/><circle cx="10" cy="10" r="3" fill="#d9d9dc"/></svg>food contact</div>
      <div class="mark"><svg class="icon" viewBox="0 0 20 20"><circle cx="10" cy="10" r="9" fill="none" stroke="#d9d9dc"/><polyline points="6,10 9,13 14,7" fill="none" stroke="#d9d9dc"/></svg>hand wash</div>
    </div>
  </section>

</main>
</body>
</html>
```